"Breathe & Bloom" Book Cover 5.5x8.5

Title of the book is "Breathe & Bloom"
Subtitle is "Unmasking Pricing Myths"
I've used PixelGuild on multiple occasions you can look on my Borvex page, Mark Delwitt, to see the covers I've used in the other projects I've done.
The target audience are people who have been tricked to think they can't retire because inflation, i.e. cost of living is going up so much they must work to keep up. There is no evidence of this.
And those are the people I want to reach so they can "Breathe...and Bloom."
Target Market(s)
Americans aged 55 and over who are thinking about retirement
Industry/Entity Type
Financial
Requirements
Nice to have
- Keep It Simple, Stupid is my mantra. Just make it pop out when people are browsing
Should not have
- No piggy banks. No old people sitting on a beach.

```html
<!DOCTYPE html>
<html lang="en">
<head>
<meta charset="utf-8">
<title>Breathe &amp; Bloom — Book Cover</title>
<link rel="stylesheet" href="https://fonts.googleapis.com/css2?family=Abril+Fatface&family=Playfair+Display:ital,wght@1,400&family=Montserrat:wght@300&family=Libre+Baskerville&display=swap">
<style>
  :root {
    --ink-sage: #66736a;
    --ink-mist: #a4aca5;
    --accent-gold: #d4ae3c;
    --paper: #ffffff;
    --band-line: #a5aca5;
    --band-dark: #66736a;
    --art-tone: #e4e8e4;
    --art-edge: #f6f7f6;
  }
  html, body {
    margin: 0;
    padding: 0;
    overflow: hidden;
    background: var(--paper);
  }
  .cover {
    position: relative;
    width: 776px;
    height: 1200px;
    background: var(--paper);
    overflow: hidden;
  }
  .title-block {
    position: absolute;
    left: 0;
    top: 0;
    width: 776px;
    height: 470px;
  }
  .title-word {
    font-family: "Abril Fatface", "Playfair Display", serif;
    fill: var(--ink-sage);
  }
  .title-amp {
    font-family: "Playfair Display", serif;
    font-style: italic;
    fill: var(--ink-mist);
  }
  .subtitle {
    position: absolute;
    left: 0;
    width: 776px;
    top: 478px;
    margin: 0;
    text-align: center;
    font-family: "Montserrat", sans-serif;
    font-weight: 300;
    font-size: 41px;
    letter-spacing: 0.3px;
    color: var(--accent-gold);
  }
  .hero-art {
    position: absolute;
    left: 67px;
    top: 578px;
    width: 646px;
    height: 465px;
    border-radius: 24px;
    background: linear-gradient(180deg, var(--art-edge) 0%, var(--art-tone) 50%, var(--art-edge) 100%);
  }
  .footer-rule {
    position: absolute;
    left: 0;
    top: 1067px;
    width: 776px;
    height: 13px;
    background: var(--band-line);
  }
  .footer-band {
    position: absolute;
    left: 0;
    top: 1086px;
    width: 776px;
    height: 114px;
    background: var(--band-dark);
    display: flex;
    align-items: center;
    justify-content: center;
  }
  .author {
    margin: 0;
    font-family: "Libre Baskerville", serif;
    font-size: 40px;
    color: var(--paper);
    letter-spacing: 0.5px;
  }
</style>
</head>
<body>
  <main class="cover">
    <svg class="title-block" viewBox="0 0 776 470" aria-label="Breathe &amp; Bloom" role="heading">
      <text class="title-word" x="55" y="208" font-size="168" textLength="448" lengthAdjust="spacingAndGlyphs">Breathe</text>
      <text class="title-amp" x="462" y="318" font-size="200">&amp;</text>
      <text class="title-word" x="227" y="434" font-size="188" textLength="491" lengthAdjust="spacingAndGlyphs">Bloom</text>
    </svg>

    <h2 class="subtitle">Unmasking Pricing Myths</h2>

    <div class="hero-art" role="img" aria-label="Illustration: life ring covered in dollar bills with red bands and a white rope"></div>

    <div class="footer-rule"></div>
    <footer class="footer-band">
      <p class="author">Mark Delwitt</p>
    </footer>
  </main>
</body>
</html>
```